buseisness card

design a card that similar to my web site
TRELLINGWORKSLLC .COM

Contact Information for Business Card

NAME PHONE # WEBSITE EMAIL AND DISCTIPTION OF WHAT WE DO

Colors
0054AA
0677BA
7BADD7
CADEEF
E8F1F8

Requirements
Must have
• lOGO AND DETAILS
Nice to have
• I LIKE THE WATER LIKE ON MY WEB SITE

```html
<!DOCTYPE html>
<html lang="en">
<head>
<meta charset="utf-8">
<title>Trelling Works – Business Card</title>
<link href="https://fonts.googleapis.com/css2?family=Montserrat:wght@600;700&family=Roboto:ital,wght@0,400;0,500;1,400;1,700&display=swap" rel="stylesheet">
<style>
  :root {
    --brand-deep: #0054AA;
    --brand-mid: #0677BA;
    --brand-sky: #7BADD7;
    --brand-mist: #CADEEF;
    --brand-foam: #E8F1F8;
    --card-white: #ffffff;
    --backdrop: #1b1d22;
  }
  * { margin: 0; padding: 0; box-sizing: border-box; }
  html, body {
    width: 1200px; height: 900px; overflow: hidden;
    background: var(--backdrop);
    font-family: "Roboto", Arial, sans-serif;
  }
  .sheet {
    width: 1200px; height: 900px;
    display: flex; flex-direction: column; align-items: center; justify-content: center;
    gap: 44px;
  }
  .card {
    position: relative;
    width: 680px; height: 388px;
    border-radius: 22px;
    overflow: hidden;
    box-shadow: 0 14px 34px rgba(0,0,0,.45);
  }
  .card--front { background: var(--card-white); }
  .card__art { position: absolute; inset: 0; width: 100%; height: 100%; }

  .contact {
    position: absolute; left: 44px; top: 196px;
    color: var(--card-white);
  }
  .contact__name {
    font-weight: 700; font-style: italic; font-size: 24px;
    letter-spacing: .5px; text-transform: uppercase;
    color: var(--brand-sky);
  }
  .contact__role { font-style: italic; font-size: 15px; margin: 2px 0 12px; }
  .contact__list { list-style: none; font-size: 15px; line-height: 1.55; }
  .contact__list li { display: flex; align-items: center; gap: 8px; }
  .contact__icon { width: 12px; height: 12px; fill: var(--brand-mist); flex: none; }

  .brand-name {
    position: absolute;
    font-family: "Montserrat", Arial, sans-serif;
    font-weight: 700; letter-spacing: 2px; text-transform: uppercase;
    display: flex; align-items: center; gap: 14px;
  }
  .brand-name__dot { border-radius: 50%; flex: none; }
  .card--front .brand-name { left: 392px; top: 150px; font-size: 26px; color: var(--brand-mid); }
  .card--front .brand-name__dot { width: 22px; height: 22px; background: var(--brand-mid); }

  .address {
    position: absolute; left: 316px; bottom: 34px;
    color: var(--card-white); font-size: 15px; line-height: 1.5;
  }

  .card--back {
    background: linear-gradient(135deg, var(--brand-mid) 0%, var(--brand-deep) 100%);
    display: flex; align-items: center; justify-content: center;
  }
  .card--back .brand-name { position: static; font-size: 40px; color: var(--card-white); }
  .card--back .brand-name__dot { width: 34px; height: 34px; background: var(--brand-sky); }
</style>
</head>
<body>
<main class="sheet">

  <section class="card card--front">
    <svg class="card__art" viewBox="0 0 680 388" preserveAspectRatio="none">
      <defs>
        <linearGradient id="sea" x1="0" y1="0" x2="1" y2="1">
          <stop offset="0" stop-color="#0677BA"/>
          <stop offset="1" stop-color="#0054AA"/>
        </linearGradient>
        <linearGradient id="splash" x1="0" y1="0" x2="1" y2="1">
          <stop offset="0" stop-color="#7BADD7"/>
          <stop offset=".55" stop-color="#4fb6e8"/>
          <stop offset="1" stop-color="#CADEEF"/>
        </linearGradient>
      </defs>
      <path class="sea-field" d="M0 118 C 120 70 210 110 290 190 S 470 360 600 388 L 0 388 Z" fill="url(#sea)"/>
      <g role="img" aria-label="Water wave splash with bubbles along the edge of the blue area">
        <path d="M0 118 C 120 70 210 110 290 190 S 470 360 600 388" fill="none" stroke="url(#splash)" stroke-width="26" stroke-linecap="round" opacity=".9"/>
      </g>
    </svg>

    <div class="contact">
      <p class="contact__name">Dana Whitlow</p>
      <p class="contact__role">Founder &amp; CEO</p>
      <ul class="contact__list">
        <li><svg class="contact__icon" viewBox="0 0 12 12"><path d="M2 1h2l1 3-1.3 1a7 7 0 0 0 3.3 3.3L8 7l3 1v2a1 1 0 0 1-1 1A9 9 0 0 1 1 2a1 1 0 0 1 1-1z"/></svg>+740 555 0142</li>
        <li><svg class="contact__icon" viewBox="0 0 12 12"><path d="M1 2.5h10v7H1z M1 2.5l5 4 5-4" stroke="#CADEEF" stroke-width="1" fill="none"/></svg>hello@tw-mail.com</li>
        <li><svg class="contact__icon" viewBox="0 0 12 12"><circle cx="6" cy="6" r="5" fill="none" stroke="#CADEEF"/><path d="M1 6h10M6 1c-2.5 3-2.5 7 0 10M6 1c2.5 3 2.5 7 0 10" fill="none" stroke="#CADEEF" stroke-width=".8"/></svg>www.trellingworksllc.com</li>
      </ul>
    </div>

    <div class="brand-name"><span class="brand-name__dot"></span>Trelling Works</div>

    <p class="address">418 Harbor Crest Drive<br>Dayton, OH 45402</p>
  </section>

  <section class="card card--back">
    <div class="brand-name"><span class="brand-name__dot"></span>Trelling Works</div>
  </section>

</main>
</body>
</html>
```